Sifu Tomaso's First Book - research in Wing Chun Kung Fu

Sifu Tomaso (www.sifutomaso.example) is the founder and Worldwide Head Instructor of his Wing Chun Kung Fu organization, the GRBF. To get his extensive research out to the world, he has written his first book which counts well over 400 pages and needs to hit the shelves as soon as possible.

We are looking for a graphic designer (a cover at first, but if you think you can design the whole INSIDE of the book, we are more than happy to look at your designs!) who understands the targetgroup to which this book has to appeal: kung fu lovers, GRBF students and martial arts affiliates. The highly anticipated book counts around 400 pages and features 50/50 text and photos. It promises to have a grand impact on the martial arts community.

Front Cover Info:
Title of the book: The Nine Quiet Pillars
Undertitle: The BDR and history of Crane Palm
Writer: Sifu Tomaso Iadarola

Coloursuggestion to possibly work with: yellow and black
Think oriental/Chinese but wrapped in modern Western design. Please feel free to go crazy, though professional.
Backgroundinfo can be found on http://www.palmrivera.example/grbf/sifu-tomaso-grbf-palm-river-system/ and http://sifutomaso.example/biography/. Many additional info can be found on these websites.

Extra info:
- estimated publishing: 40.000 pax.

Attachments:
- the GRBF logo has to be on the front of the book somewhere
- the Sifu Tomaso logo (double S logo) has to be on the spine of the book

Industry/Entity Type

Graphic Designer

Requirements
Must have
• - Front cover must have image of author (see attachment) WITHOUT the Sifu Tomaso logo: the author has to look up to the book title.
• - the double S symbol of the Sifu Tomaso logo (see attachment) to be placed at the bottom of the spine of the book along with the author's name and booktitle. Note: double S logo has to be readible when the book it is vertical.

```html
<!DOCTYPE html>
<html lang="en">
<head>
<meta charset="utf-8">
<title>The Nine Quiet Pillars – Cover</title>
<link rel="stylesheet" href="https://fonts.googleapis.com/css2?family=Ubuntu:wght@400;500&family=Noto+Serif+SC:wght@300&display=swap">
<style>
  :root {
    --leather-dark: #170e0d;
    --leather-mid: #251715;
    --leather-light: #2d1c1a;
    --accent-gold: #eaa43a;
    --title-white: #f6f3f0;
    --emboss: #33241f;
    --emboss-high: #3d2d28;
    --emboss-low: #140b0a;
    --badge-white: #ffffff;
    --badge-ink: #1c1c1c;
  }
  html, body {
    margin: 0;
    padding: 0;
    width: 776px;
    height: 1200px;
    overflow: hidden;
    background: var(--leather-dark);
  }
  .cover {
    position: relative;
    width: 776px;
    height: 1200px;
    overflow: hidden;
    font-family: "Ubuntu", sans-serif;
    background:
      radial-gradient(ellipse 80% 65% at 60% 40%, var(--leather-light) 0%, var(--leather-mid) 50%, var(--leather-dark) 100%);
  }
  .subtitle {
    position: absolute;
    top: 110px;
    left: 0;
    width: 100%;
    margin: 0;
    text-align: center;
    font-size: 20px;
    line-height: 24px;
    font-weight: 400;
    letter-spacing: 5.4px;
    text-indent: 5.4px;
    color: var(--accent-gold);
    text-transform: uppercase;
  }
  .title {
    position: absolute;
    top: 354px;
    left: 0;
    width: 100%;
    margin: 0;
    text-align: center;
    font-size: 29px;
    line-height: 36px;
    font-weight: 400;
    letter-spacing: 0.3px;
    color: var(--title-white);
    text-transform: uppercase;
  }
  .style-glyphs {
    position: absolute;
    top: 505px;
    left: 0;
    width: 100%;
    text-align: center;
    font-family: "Noto Serif SC", serif;
    font-weight: 300;
    font-size: 140px;
    line-height: 180px;
    letter-spacing: 10px;
    text-indent: -10px;
    color: var(--emboss);
    text-shadow: 1px 1px 0 var(--emboss-high), -1px -1px 0 var(--emboss-low);
  }
  .author-mark {
    position: absolute;
    top: 985px;
    left: 0;
    width: 100%;
    text-align: center;
    font-size: 22px;
    line-height: 30px;
    font-weight: 500;
    letter-spacing: 1px;
    color: var(--accent-gold);
    text-transform: uppercase;
  }
  .author {
    position: absolute;
    top: 1045px;
    left: 0;
    width: 100%;
    margin: 0;
    text-align: center;
    font-size: 19px;
    line-height: 24px;
    font-weight: 400;
    color: var(--accent-gold);
    text-transform: uppercase;
  }
  .org-badge {
    position: absolute;
    top: 1094px;
    left: 348px;
    width: 87px;
    height: 24px;
    background: var(--badge-white);
    color: var(--badge-ink);
    font-size: 13px;
    font-weight: 500;
    line-height: 24px;
    text-align: center;
    letter-spacing: 1px;
  }
</style>
</head>
<body>
  <main class="cover">
    <p class="subtitle">The BDR and history of Crane Palm</p>
    <h1 class="title">The Nine Quiet Pillars</h1>
    <div class="style-glyphs" lang="zh">鹤掌</div>
    <div class="author-mark">Tomaso</div>
    <p class="author">Sifu Tomaso Venturelli</p>
    <div class="org-badge">GRBF</div>
  </main>
</body>
</html>
```